VELORA toner box Packaging and inkcartridge Packaging Design

We are a sales printer supplies company, our logo is VELORA, to design toner cartridges packaging, ink cartridges packaging,Online supply platform, the store not only has many branded goods, but also provide more than a thousand kinds of photocopy paper, printers, office machines, office supplies and other goods

Target Market(s)

printer ink cartridge / toner cartridge

Industry/Entity Type

Printer

Font styles to use
Decorative

Colors
33a6d7
add136
b768aa

Requirements
Must have
• Velora logo

```html
<!DOCTYPE html>
<html lang="en">
<head>
<meta charset="utf-8">
<title>Velora Cartridge Combo Pack – Box Dieline</title>
<link href="https://fonts.googleapis.com/css2?family=Open+Sans:ital,wght@0,400;0,600;0,700;0,800;1,700&family=Arimo:wght@400;700&display=swap" rel="stylesheet">
<style>
  :root{
    --panel:#f4f4f5;
    --ink-cyan:#33a6d7;
    --ink-magenta:#e2168c;
    --ink-yellow:#f5e400;
    --ink-black:#111;
    --tone-green:#add136;
    --tone-orange:#f7a23b;
    --tone-pink:#d64b74;
    --tone-blue:#33a6d7;
    --brand-green:#6fb32e;
    --brand-dot:#f7a23b;
    --text-dark:#222;
    --text-grey:#555;
  }
  html,body{margin:0;padding:0;overflow:hidden;background:#fff;}
  .canvas{position:relative;width:1200px;height:848px;overflow:hidden;background:#fff;font-family:"Open Sans",sans-serif;}
  .dieline,.colour-wash{position:absolute;left:0;top:0;}
  .colour-wash{left:248px;top:340px;}

  .facts{position:absolute;left:270px;top:361px;width:206px;border:2px solid var(--text-dark);font-family:"Arimo",sans-serif;color:var(--text-dark);background:rgba(255,255,255,.55);}
  .facts-title{font-weight:700;font-size:17px;line-height:19px;padding:2px 4px 0;}
  .facts-size{font-size:11px;line-height:13px;padding:0 4px 2px;border-bottom:3px solid var(--text-dark);}
  .facts-row{font-size:11.5px;line-height:12.5px;padding:2px 4px;border-bottom:1px solid var(--text-dark);display:flex;justify-content:space-between;gap:4px;}
  .facts-row:last-child{border-bottom:none;}
  .facts-row span:last-child{white-space:nowrap;}
  .care-note{position:absolute;left:282px;top:546px;width:170px;border:1px solid var(--text-dark);padding:2px 3px;font-family:"Arimo",sans-serif;font-size:7.5px;line-height:9.5px;color:var(--text-grey);text-align:justify;background:rgba(255,255,255,.5);}
  .maker{position:absolute;left:255px;top:606px;font-size:10.5px;color:var(--text-grey);line-height:16px;}
  .maker strong{display:block;color:#333;font-weight:700;margin-bottom:4px;}

  .cmyk-strip{position:absolute;display:flex;gap:3px;}
  .cmyk-strip span{width:20px;height:21px;display:flex;align-items:center;justify-content:center;font-weight:800;font-size:13px;color:#fff;}
  .cmyk-strip .c{background:var(--ink-cyan);}
  .cmyk-strip .m{background:var(--ink-magenta);}
  .cmyk-strip .y{background:var(--ink-yellow);color:#111;}
  .cmyk-strip .k{background:var(--ink-black);}
  .cmyk-front{left:763px;top:343px;}
  .cmyk-side{left:978px;top:523px;flex-direction:column;gap:10px;}

  .combo-label{position:absolute;font-weight:700;font-style:italic;font-size:14px;color:var(--text-dark);white-space:nowrap;}
  .combo-front{left:766px;top:366px;}
  .combo-side{left:956px;top:652px;font-size:17px;line-height:22px;transform:rotate(-90deg);transform-origin:left top;}

  .brand{position:absolute;color:var(--brand-green);white-space:nowrap;}
  .brand-name{font-weight:800;font-size:64px;line-height:64px;letter-spacing:-1px;}
  .brand-dot{display:inline-block;width:12px;height:12px;border-radius:50%;background:var(--brand-dot);vertical-align:top;margin:6px 0 0 4px;}
  .brand-type{font-weight:800;font-size:24px;line-height:24px;}
  .brand-note{color:#111;font-weight:600;font-size:11px;line-height:14px;}
  .brand-front{left:652px;top:560px;}
  .brand-front .brand-type{margin-left:62px;}
  .brand-front .brand-note{margin-left:120px;}

  .brand-side{left:912px;top:502px;width:160px;transform:rotate(-90deg);transform-origin:left top;}
  .brand-side .brand-name{font-size:52px;line-height:46px;}
  .brand-side .brand-dot{width:10px;height:10px;margin-top:4px;}
  .brand-side .brand-type{font-size:21px;line-height:23px;text-align:right;}
  .brand-side .brand-note{font-size:10px;line-height:13px;text-align:right;}
</style>
</head>
<body>
<div class="canvas">
  <svg class="dieline" width="1200" height="848" viewBox="0 0 1200 848" xmlns="http://www.w3.org/2000/svg">
    <defs>
      <linearGradient id="flap" x1="0" x2="1" y1="0" y2="0">
        <stop offset="0" stop-color="#1a1a1a"/><stop offset=".5" stop-color="#333"/><stop offset="1" stop-color="#1a1a1a"/>
      </linearGradient>
      <linearGradient id="glue" x1="0" x2="1"><stop offset="0" stop-color="#d4d5d6"/><stop offset="1" stop-color="#a9abad"/></linearGradient>
    </defs>

    <g class="flaps" fill="url(#flap)">
      <path class="tuck-top" d="M255,38 H485 V340 H255 Z"/>
      <path class="lid-front" d="M625,340 V215 Q625,157 685,157 H800 Q860,157 860,215 V340 Z"/>
      <path class="dust-left" d="M492,340 V322 L498,318 L515,250 H600 L625,318 V340 Z"/>
      <path class="dust-right" d="M865,340 V250 H975 L995,318 L1000,322 V340 Z"/>
      <path class="bottom-side" d="M248,700 H490 V712 L478,728 H455 L430,760 V808 H248 Z"/>
      <path class="bottom-narrow-left" d="M490,700 H625 V790 H512 Q505,745 490,725 Z"/>
      <path class="bottom-front" d="M625,700 H860 L848,728 H810 L785,760 V808 H630 Z"/>
      <path class="bottom-narrow-right" d="M865,700 H1000 V715 L985,790 H887 Q882,745 865,722 Z"/>
    </g>

    <g class="hanger" fill="#fff">
      <line x1="255" y1="204" x2="485" y2="204" stroke="#fff" stroke-width="2"/>
      <rect x="315" y="150" width="100" height="16" rx="8"/><circle cx="365" cy="158" r="14"/>
      <rect x="315" y="237" width="100" height="16" rx="8"/><circle cx="365" cy="245" r="14"/>
      <path d="M625,210 h10 v5 h10 M860,210 h-10 v5 h-10" stroke="#fff" fill="none"/>
    </g>

    <path class="glue-flap" d="M212,350 L248,340 V700 L212,690 Z" fill="url(#glue)"/>
    <rect class="body" x="248" y="340" width="752" height="360" fill="var(--panel)"/>
  </svg>

  <svg class="colour-wash" width="752" height="360" viewBox="0 0 752 360" role="img" aria-label="Fanned rainbow light rays in green, orange, pink and blue spreading from the right edge">
    <defs>
      <linearGradient id="wash-tones" x1="0" y1="0" x2="0" y2="1">
        <stop offset="0" stop-color="var(--tone-blue)" stop-opacity=".28"/>
        <stop offset=".22" stop-color="var(--tone-green)" stop-opacity=".3"/>
        <stop offset=".4" stop-color="var(--tone-orange)" stop-opacity=".28"/>
        <stop offset=".55" stop-color="var(--tone-pink)" stop-opacity=".26"/>
        <stop offset=".72" stop-color="var(--tone-orange)" stop-opacity=".26"/>
        <stop offset="1" stop-color="var(--tone-blue)" stop-opacity=".26"/>
      </linearGradient>
      <linearGradient id="wash-fade" x1="0" x2="1">
        <stop offset="0" stop-color="#fff" stop-opacity=".55"/>
        <stop offset=".45" stop-color="#fff" stop-opacity="0"/>
        <stop offset="1" stop-color="#fff" stop-opacity=".6"/>
      </linearGradient>
    </defs>
    <rect width="752" height="360" fill="url(#wash-tones)"/>
    <rect width="752" height="360" fill="url(#wash-fade)"/>
  </svg>

  <div class="facts">
    <div class="facts-title">Product Facts</div>
    <div class="facts-size">Pack Size : 4 Cartridges</div>
    <div class="facts-row"><span>Contents Per Pack</span></div>
    <div class="facts-row"><span>Black pigment ink<br>cartridge, high yield</span><span>18ml*</span></div>
    <div class="facts-row"><span>Cyan, magenta, yellow<br>dye ink colours</span><span>12ml*</span></div>
    <div class="facts-row"><span>Page yield per set<br>(ISO 5% coverage)</span><span>500pg*</span></div>
    <div class="facts-row"><span>Yield figures are approximate</span></div>
  </div>
  <div class="care-note">Compatible cartridges are not made or endorsed by the printer maker. Names are used only to show fit. Store in a cool, dry place and use before date.</div>
  <div class="maker"><strong>Manufacturer :</strong>Norvale Labs Ltd - 41 Harwick Ave.<br>Lakeford, ON L0K 2P4, Canada</div>

  <div class="cmyk-strip cmyk-front"><span class="c">C</span><span class="m">M</span><span class="y">Y</span><span class="k">K</span></div>
  <div class="combo-label combo-front">Combo Pack</div>
  <div class="brand brand-front">
    <div class="brand-name">Velora<span class="brand-dot"></span></div>
    <div class="brand-type">CARTRIDGE</div>
    <div class="brand-note">Compatible with</div>
  </div>

  <div class="brand brand-side">
    <div class="brand-name">Velora<span class="brand-dot"></span></div>
    <div class="brand-type">CARTRIDGE</div>
    <div class="brand-note">Compatible with</div>
  </div>
  <div class="combo-label combo-side">Combo Pack</div>
  <div class="cmyk-strip cmyk-side"><span class="c">C</span><span class="m">M</span><span class="y">Y</span><span class="k">K</span></div>
</div>
</body>
</html>
```